Clone http://www.pebbledeskwriter.com/ (fully functioning WordPress website - not just design)

1) Clone or recreate http://www.pebbledeskwriter.com/ in Wordpress with WooCommerece plugin
2) Connect to our Existing Quendo Account
3) Make site-wide text only changes that we provide you when site is complete.

We will provide all the graphics according to your size requirements.

Cash awarded to the closest copy of http://www.pebbledeskwriter.com/

Target Market(s)

WordPress developer

Number of Pages Required

5+ page

Font styles to use
Sans Serif

Colors
abd037
cadf82
eaf2ce

Requirements
Must have
• Fully functioning website.

```html
<!DOCTYPE html>
<html lang="en">
<head>
<meta charset="utf-8">
<title>PebbleDesk Writer – Easy, Online Mail Merge</title>
<link rel="stylesheet" href="https://fonts.googleapis.com/css2?family=Lato:wght@300;400;700&display=swap">
<style>
:root{
  --green:#abd037;
  --green-mid:#cadf82;
  --green-pale:#eaf2ce;
  --green-title:#3fa81e;
  --ink:#222;
  --body:#555;
  --heading-grey:#555;
  --hero-dark:#2a0d08;
  --hero-mid:#5a2417;
  --topbar:#2b2b2b;
  --footer:#ececec;
  --footer-base:#d9d9d9;
  --card-line:#e2e2e2;
}
*{box-sizing:border-box;margin:0;padding:0}
html,body{width:1200px;height:2503px;overflow:hidden}
body{position:relative;font-family:"Lato",sans-serif;color:var(--body);background:#fff}
.abs{position:absolute}

.top-bar{left:0;top:0;width:1200px;height:27px;background:var(--topbar)}
.top-bar a{position:absolute;top:6px;font-size:12px;font-weight:700;color:#fff;text-decoration:none}

.hero{left:0;top:27px;width:1200px;height:702px;
  background:radial-gradient(ellipse at 70% 40%,#6a2c1c 0%,var(--hero-mid) 35%,var(--hero-dark) 100%)}
.hero-scene{left:430px;top:160px;width:770px;height:380px;border-radius:8px;
  background:radial-gradient(ellipse at 45% 40%,rgba(200,200,205,.35) 0%,rgba(120,80,60,.2) 45%,rgba(0,0,0,0) 75%)}

.brand{left:129px;top:70px;display:flex;align-items:center;gap:10px}
.brand-dot{width:22px;height:22px;border-radius:50%;background:var(--green)}
.brand-name{font-size:20px;font-weight:700;color:var(--green)}

.nav a{position:absolute;top:73px;height:37px;line-height:37px;text-align:center;
  background:#050505;color:#fff;font-size:13px;font-weight:700;text-decoration:none;border-radius:3px}

.hero-title{left:121px;top:205px;font-size:57px;line-height:88px;font-weight:700;color:#fff}
.btn{display:block;text-align:center;color:#fff;text-decoration:none;font-size:18px;
  background:linear-gradient(#c4e063,#8cbb2a);border-radius:3px}
.hero-btn{left:121px;top:402px;width:241px;height:39px;line-height:39px}
.hero-note{left:121px;top:457px;font-size:13px;color:#fff}
.hero-question{left:121px;top:560px;font-size:19px;color:var(--green)}
.hero-text{left:121px;top:600px;width:760px;font-size:16px;line-height:30px;color:#fff}

.section-title{left:0;top:843px;width:1200px;text-align:center;font-size:41px;font-weight:300;color:var(--heading-grey)}

.step{left:121px;width:959px;height:265px;background:#fff;border:1px solid var(--card-line);
  box-shadow:0 2px 5px rgba(0,0,0,.12)}
.step-corner{position:absolute;top:0;width:115px;height:115px}
.step-corner.left{left:0}
.step-corner.right{right:0}
.step-num{position:absolute;top:8px;font-size:52px;font-weight:300;color:var(--green-title)}
.step-body{position:absolute;top:40px;width:400px}
.step-title{font-size:32px;font-weight:400;color:var(--green-title);line-height:38px}
.step-sub{font-size:17px;font-weight:700;color:var(--ink);margin-top:2px}
.step-text{font-size:13.5px;line-height:23.5px;color:#666;margin-top:6px}
.step-visual{position:absolute;border:1px solid #ccc;box-shadow:0 3px 6px rgba(0,0,0,.25)}

.cta-btn{left:479px;top:2091px;width:242px;height:40px;line-height:40px}
.cta-note{left:0;top:2139px;width:1200px;text-align:center;font-size:13px;color:#777}

.footer{left:0;top:2230px;width:1200px;height:225px;background:var(--footer)}
.footer h4{position:absolute;font-size:17px;font-weight:400;color:#222}
.footer ul{position:absolute;list-style:disc;padding-left:14px;font-size:13px;line-height:28px;color:#222}
.footer .credit{position:absolute;font-size:13px;line-height:22px;color:#222}
.social{position:absolute;top:2331px}
.footer-base{left:0;top:2455px;width:1200px;height:48px;background:var(--footer-base);
  font-size:13px;line-height:48px;padding-left:121px;color:#555}
</style>
</head>
<body>

<div class="abs top-bar">
  <a style="left:994px">Login</a>
  <a style="left:1038px">Register</a>
</div>

<div class="abs hero" role="img" aria-label="Dark wooden desk photo with an open laptop, coffee cup, USB stick, ID card and drawing tablet"></div>
<div class="abs hero-scene" role="img" aria-label="Laptop, coffee and drawing tablet laid out on the desk"></div>

<div class="abs brand"><span class="brand-dot"></span><span class="brand-name">PebbleDesk</span></div>

<nav class="nav">
  <a style="left:514px;width:84px">Home</a>
  <a style="left:624px;width:76px;color:#f2e27a">Tour</a>
  <a style="left:727px;width:80px">Price</a>
  <a style="left:830px;width:111px">Our Team</a>
  <a style="left:964px;width:116px">Contact Us</a>
</nav>

<h1 class="abs hero-title">Easy, Online<br>Mail Merge</h1>
<a class="abs btn hero-btn">Start Free Trail</a>
<p class="abs hero-note">Start building your mail merge online now!</p>
<p class="abs hero-question">Do you have a letter you need to send out to multiple people?</p>
<p class="abs hero-text">Mail merge is the automatic addition of names and addresses from a spreadsheet to letters and envelopes in order to facilitate sending personalised mail to many people.</p>

<h2 class="abs section-title">100% Easier Than Using PageForge Desk!</h2>

<section class="abs step" style="top:1009px">
  <svg class="step-corner left" viewBox="0 0 115 115"><defs><linearGradient id="g1" x1="0" y1="0" x2="1" y2="1"><stop offset="0" stop-color="#cadf82"/><stop offset="1" stop-color="#4fb52a"/></linearGradient></defs><polygon points="0,0 115,0 0,115" fill="url(#g1)"/></svg>
  <span class="step-num" style="left:14px">1</span>
  <div class="step-body" style="left:92px">
    <h3 class="step-title">Upload Your Data</h3>
    <p class="step-sub">Create a list of addresses, names or other data</p>
    <p class="step-text">Just copy and paste or type your data about your clients such as their name, address and any other associated fields into our in browser spreadsheet. You can even upload your data as a CSV file! It couldn't be easier. Your data is easy to manage and best yet, it's all backed up in the cloud.</p>
  </div>
  <div class="step-visual" style="left:543px;top:14px;width:346px;height:227px;background:linear-gradient(#ffffff,#cde9f7)" role="img" aria-label="Illustration of a cloud of files syncing with a phone and a laptop"></div>
</section>

<section class="abs step" style="top:1370px">
  <svg class="step-corner right" viewBox="0 0 115 115"><defs><linearGradient id="g2" x1="1" y1="0" x2="0" y2="1"><stop offset="0" stop-color="#cadf82"/><stop offset="1" stop-color="#4fb52a"/></linearGradient></defs><polygon points="0,0 115,0 115,115" fill="url(#g2)"/></svg>
  <span class="step-num" style="right:14px">2</span>
  <div class="step-visual" style="left:37px;top:36px;width:354px;height:202px;background:linear-gradient(#e4e4e4,#f7f7f7)" role="img" aria-label="Screenshot of the template editor with a sample envelope design"></div>
  <div class="step-body" style="left:517px;width:400px">
    <h3 class="step-title">Design Your Template</h3>
    <p class="step-sub">Build your document in your browser, it's easy</p>
    <p class="step-text">You can build any document in our easy to use editor. Choose from a range of paper sizes like A4, C4 Envelope, US Letter or specify your own. Drag and drop the variables from your uploaded data right onto your page. Scan or upload an existing PDF or DocX document to be used as your page background. Best of all you can reuse the template again and again.</p>
  </div>
</section>

<section class="abs step" style="top:1758px">
  <svg class="step-corner left" viewBox="0 0 115 115"><polygon points="0,0 115,0 0,115" fill="url(#g1)"/></svg>
  <span class="step-num" style="left:14px">3</span>
  <div class="step-body" style="left:92px">
    <h3 class="step-title">Merge to PDF</h3>
    <p class="step-sub">Combine it all into a PDF ready for print</p>
    <p class="step-text">We'll automatically combine your data with your template, producing a unique page or set of pages for each row. Then it's easy to print off your PDF and mail out your pages. You can create anything from personally addressed advertising to invoices and pre filled forms.</p>
  </div>
  <div class="step-visual" style="left:533px;top:14px;width:356px;height:217px;background:linear-gradient(#f2f2f2,#dedede)" role="img" aria-label="Screenshot of a merged PDF page with a prompt to view the PDF"></div>
</section>

<a class="abs btn cta-btn">Start Free Trail</a>
<p class="abs cta-note">Start building your mail merge online now!</p>

<footer class="abs footer">
  <h4 style="left:121px;top:55px">Browse</h4>
  <ul style="left:121px;top:82px"><li>Privacy Policy</li><li>Terms and Conditions</li></ul>
  <ul style="left:374px;top:57px"><li>Refund Policy</li></ul>
  <h4 style="left:627px;top:55px">Connect with us</h4>
  <h4 style="left:879px;top:55px">PDW was created by</h4>
  <p class="credit" style="left:879px;top:82px">Lena M.<br>lena.mora@pebbledeskwriter.com</p>
</footer>

<svg class="social" style="left:624px" width="156" height="44" viewBox="0 0 156 44">
  <line x1="22" y1="22" x2="134" y2="22" stroke="#bbb" stroke-width="2"/>
  <circle cx="25" cy="22" r="19" fill="#dcdcdc" stroke="#c4c4c4" stroke-width="2"/>
  <circle cx="25" cy="22" r="12" fill="#8cbb2a"/>
  <circle cx="78" cy="22" r="19" fill="#dcdcdc" stroke="#c4c4c4" stroke-width="2"/>
  <circle cx="78" cy="22" r="12" fill="#8cbb2a"/>
  <circle cx="131" cy="22" r="19" fill="#dcdcdc" stroke="#c4c4c4" stroke-width="2"/>
  <rect x="119" y="13" width="24" height="18" rx="2" fill="#8cbb2a"/>
  <polyline points="119,14 131,24 143,14" fill="none" stroke="#fff" stroke-width="2"/>
</svg>

<div class="abs footer-base">© Copyright 2017 Corvid Labs. All Rights Reserved</div>

</body>
</html>
```